Corvant Systems Business Card

Create an appealing and elegant Business card for corvant systems. Include logo and use related colors from website, be creative. Include Business name, my name, tile, address, contacts, address, and social media contacts if possible. Logo PSD file is attached.

Bleed Area: 3.46" x 2.32"
Trim: 3.3" x 2.16"
Safe Area: 3.14" x 2.02"

Save files as vector-based PDF with outlined text and PNG.
No crop marks
CMYK color setting

Business Card Info:

Corvant Systems

Dennis Halvorsen
Owner

512 Brindlemoor Rd Unit C
Merrow Falls, VT 02871
t. 1.888.555.0162
e. dennis.h@corvantsys.example
w. www.corvantsys.example

facebook. www.facebook.com/CorvantSys
twitter. twitter.com/corvantsys
pinterest. www.pinterest.com/corvantsys/

Target Market(s)

Business Owners and Partners

Industry/Entity Type

Business

Requirements
Must have
• Logo and related colors from website

```html
<!DOCTYPE html>
<html lang="en">
<head>
<meta charset="utf-8">
<title>Corvant Systems Business Card</title>
<link rel="stylesheet" href="https://fonts.googleapis.com/css2?family=Source+Sans+3:wght@400;600&display=swap">
<style>
  :root {
    --band-blue: #7699c0;
    --icon-blue: #4c70a8;
    --contact-grey: #a69f91;
    --paper: #ffffff;
    --ink: #111111;
    --rule: #e6e6e6;
  }
  html, body {
    margin: 0;
    padding: 0;
    overflow: hidden;
    background: var(--paper);
  }
  .card {
    position: relative;
    width: 1200px;
    height: 787px;
    background: var(--paper);
    overflow: hidden;
    font-family: "Source Sans 3", "Myriad Pro", sans-serif;
  }
  .band {
    position: absolute;
    left: 0;
    width: 100%;
    background: var(--band-blue);
  }
  .band--top { top: 0; height: 80px; }
  .band--bottom { top: 708px; height: 79px; }

  .brand {
    position: absolute;
    left: 58px;
    top: 96px;
    width: 490px;
    color: var(--ink);
    font-weight: 600;
    line-height: 1;
  }
  .brand__line {
    display: block;
    font-size: 112px;
    letter-spacing: 1px;
  }
  .brand__line + .brand__line { margin-top: 8px; }
  .brand-rule {
    position: absolute;
    left: 28px;
    top: 336px;
    width: 542px;
    height: 1px;
    background: var(--rule);
  }

  .person {
    position: absolute;
    right: 38px;
    top: 92px;
    text-align: right;
    color: var(--ink);
    line-height: 1;
  }
  .person__name { font-size: 53px; font-weight: 400; }
  .person__title { font-size: 39px; font-weight: 400; margin-top: 0; }

  .contact-panel {
    position: absolute;
    left: 0;
    top: 345px;
    width: 100%;
    height: 302px;
    background: var(--contact-grey);
    color: var(--paper);
  }
  .contact-list,
  .social-list {
    position: absolute;
    margin: 0;
    padding: 0;
    list-style: none;
    font-size: 34px;
    line-height: 41px;
    white-space: nowrap;
  }
  .contact-list { left: 82px; top: 46px; }
  .social-list { left: 631px; top: 46px; font-size: 33px; }
  .social-list li { margin-bottom: 38px; }

  .icon {
    position: absolute;
    width: 42px;
    height: 42px;
  }
  .icon--mail { left: 32px; top: 45px; }
  .icon--friends { left: 583px; top: 47px; }
  .icon--chirp { left: 583px; top: 125px; }
  .icon--pins { left: 583px; top: 204px; }
</style>
</head>
<body>
<div class="card">
  <div class="band band--top"></div>

  <div class="brand" aria-label="Corvant Systems">
    <span class="brand__line">Corvant</span>
    <span class="brand__line">Systems</span>
  </div>
  <div class="brand-rule"></div>

  <div class="person">
    <div class="person__name">Dennis Halvorsen</div>
    <div class="person__title">Owner</div>
  </div>

  <section class="contact-panel">
    <svg class="icon icon--mail" viewBox="0 0 42 42" aria-hidden="true">
      <circle cx="21" cy="21" r="21" fill="var(--icon-blue)"/>
      <rect x="11" y="14" width="20" height="14" rx="1.5" fill="#ffffff"/>
      <path d="M11.5 15 L21 22.5 L30.5 15" fill="none" stroke="var(--icon-blue)" stroke-width="2"/>
    </svg>
    <ul class="contact-list">
      <li>512 Brindlemoor Rd Unit C</li>
      <li>Merrow Falls, VT 02871</li>
      <li>t. 1.888.555.0162</li>
      <li>e. dennis.h@corvantsys.example</li>
      <li>w. www.corvantsys.example</li>
    </ul>

    <svg class="icon icon--friends" viewBox="0 0 42 42" aria-hidden="true">
      <circle cx="21" cy="21" r="21" fill="var(--icon-blue)"/>
    </svg>
    <svg class="icon icon--chirp" viewBox="0 0 42 42" aria-hidden="true">
      <circle cx="21" cy="21" r="21" fill="var(--icon-blue)"/>
    </svg>
    <svg class="icon icon--pins" viewBox="0 0 42 42" aria-hidden="true">
      <circle cx="21" cy="21" r="21" fill="var(--icon-blue)"/>
    </svg>
    <ul class="social-list">
      <li>www.friendlink.example/CorvantSys</li>
      <li>chirpline.example/corvantsys</li>
      <li>www.pinboardly.example/corvantsys/</li>
    </ul>
  </section>

  <div class="band band--bottom"></div>
</div>
</body>
</html>
```